Restaurant needs a vertical banner for fried catfish

Our restaurant is looking for an eye-catching 78.75in. x 36in. vertical physical banner ad for our fried catfish. Photos for the fried catfish will be provided as a reference but we will also accept anything similar to the photo. We will be using the following as our receptacle: https://www.plorvista.com/banner-stand/retractable-banner-stands/
The design must incorporate the following flavor texts:
Fried Catfish
Always Fresh!
Made from Scratch
Hand-cut Fillets
The Best Catfish in Texas
Served with fries, hush puppies, and a 32oz fountain drink
Also available by the pound!
The final design should be creative, professional, and eye-catching for customers.
Updates
Need extra days to review
Colors
Designer to choose colors to be used in the design.
Requirements
Must have
- We are open to any and all design elements, albeit the 'flavor texts' should not overpower, but complement the fried catfish photo. 'Fried Catfish' can be used in lieu of a main title/logo.
Nice to have
- Transparent or textured backgrounds that can encompass any or all part of the banner such as a cutting board, shadows, abstract, etc to show depth are a plus.
- Use of vectors or objects such as ribbons or shapes to encapsulate the 'flavor texts' are also encouraged.

```html
<!DOCTYPE html>
<html lang="en">
<head>
<meta charset="utf-8">
<title>Fried Catfish Banner</title>
<link rel="stylesheet" href="https://fonts.googleapis.com/css2?family=Yellowtail&family=Montserrat:wght@500;600;700&display=swap">
<style>
  :root {
    --orange-light: #fcc53a;
    --orange: #f8b21a;
    --orange-deep: #f29a0c;
    --white: #ffffff;
    --ink: #3b3733;
    --brown: #4a3a28;
  }
  * { margin: 0; padding: 0; box-sizing: border-box; }
  html, body { width: 1200px; height: 2624px; overflow: hidden; }
  body {
    position: relative;
    font-family: 'Montserrat', sans-serif;
    background: radial-gradient(ellipse 80% 55% at 50% 50%, var(--orange-light) 0%, var(--orange) 55%, var(--orange-deep) 100%);
  }
  .script { font-family: 'Yellowtail', 'Brush Script MT', cursive; font-weight: 400; white-space: nowrap; }
  .title-fried {
    position: absolute; left: 100px; width: 1000px; top: 60px;
    text-align: center;
    font-size: 380px; line-height: 1;
    color: var(--white);
    text-shadow: 6px 8px 12px rgba(120, 60, 0, 0.25);
    transform: rotate(-8deg);
  }
  .title-catfish {
    position: absolute; left: 650px; width: 360px; top: 440px;
    text-align: center;
    font-size: 140px; line-height: 1;
    color: var(--ink);
    transform: rotate(-8deg);
  }
  .tagline {
    position: absolute; left: 0; width: 1200px; top: 660px;
    text-align: center;
    font-size: 100px; font-weight: 600; line-height: 1.1;
    color: var(--white);
    white-space: nowrap;
  }
  .ribbon {
    position: absolute; height: 68px;
    background: var(--white);
    display: flex; align-items: center;
    font-size: 52px; font-weight: 500; color: var(--ink);
    white-space: nowrap;
    box-shadow: 0 4px 10px rgba(120, 60, 0, 0.2);
  }
  .ribbon .dot {
    width: 40px; height: 40px; border-radius: 50%;
    background: var(--orange); flex: none;
  }
  .ribbon-left {
    left: 0; top: 878px; width: 545px;
    border-radius: 0 34px 34px 0;
    padding-left: 6px; padding-right: 20px;
    justify-content: space-between;
  }
  .ribbon-right {
    right: 0; top: 1000px; width: 720px;
    border-radius: 34px 0 0 34px;
    padding-left: 20px; gap: 48px;
  }
  .food-photo {
    position: absolute; left: 0; top: 1150px; width: 1180px; height: 900px;
  }
  .slogan {
    position: absolute; left: 0; width: 1200px; top: 2070px;
    text-align: center;
    font-size: 112px; line-height: 1;
    color: var(--brown);
  }
  .by-pound {
    position: absolute; left: 0; width: 1200px; top: 2188px;
    text-align: center;
    font-size: 62px; font-weight: 500; line-height: 1.1;
    color: var(--white);
    white-space: nowrap;
  }
  .served-band {
    position: absolute; left: 40px; right: 40px; top: 2378px; height: 54px;
    background: var(--white);
    display: flex; align-items: center; justify-content: center;
    font-size: 35px; font-weight: 700; color: var(--ink);
    white-space: nowrap;
  }
</style>
</head>
<body>
  <div class="title-fried script">Fried</div>
  <div class="title-catfish script">Catfish</div>
  <div class="tagline">Always Fresh!</div>

  <div class="ribbon ribbon-left"><span>Hand-cut Fillets</span><span class="dot"></span></div>
  <div class="ribbon ribbon-right"><span class="dot"></span><span>Made from Scratch</span></div>

  <svg class="food-photo" role="img" aria-label="Plate of fried catfish fillets with french fries, hush puppies, tartar sauce, lemon halves and tomatoes" viewBox="0 0 1180 900">
    <defs>
      <radialGradient id="platter" cx="50%" cy="50%" r="50%">
        <stop offset="0%" stop-color="#c97f26"/>
        <stop offset="60%" stop-color="#e0a84a"/>
        <stop offset="100%" stop-color="#f4efe6" stop-opacity="0.9"/>
      </radialGradient>
    </defs>
    <ellipse cx="590" cy="450" rx="560" ry="330" fill="url(#platter)"/>
  </svg>

  <div class="slogan script">The Best Catfish in Texas</div>
  <div class="by-pound">Also available by the pound!</div>

  <div class="served-band">Served with fries, hush puppies, and a 32oz fountain drink</div>
</body>
</html>
```